Newsletter template

I am looking for 2 newsletter templates. My website is in Wordpress and I want to use in mailchimp for lists.

One newsletter is for local clients of design remodeling firm to be sent monthly

Second newsletter is for web store offerings to be sent weekly.

Target Market(s)

Luxury home and leisure

Industry/Entity Type

Store

Requirements
Must have
• Use logos and colors to seamlessly integrate with website,

```html
<!DOCTYPE html>
<html lang="en">
<head>
<meta charset="utf-8">
<title>Maren Vale Newsletter Templates</title>
<link href="https://fonts.googleapis.com/css2?family=Montserrat:wght@300;400;600;700;800&family=Open+Sans:wght@400;600&family=Roboto+Slab:wght@700&display=swap" rel="stylesheet">
<style>
:root{
  --canvas:#dcdcdc;
  --paper:#ffffff;
  --band:#efefef;
  --ink:#222222;
  --teal:#1fa3bf;
  --sky:#4ec0e6;
  --green:#8ec63f;
  --lime:#9ccc1c;
  --red:#e8343c;
  --coral:#f05a5b;
  --gold:#e4b43a;
}
*{margin:0;padding:0;box-sizing:border-box}
html,body{width:1200px;height:1000px;overflow:hidden;background:var(--canvas)}
body{position:relative;font-family:"Montserrat",Arial,sans-serif;color:var(--ink)}
.abs{position:absolute}
.label{position:absolute;top:36px;font:600 14px/1 "Montserrat",Arial,sans-serif;letter-spacing:.5px;color:#111}
.sheet{position:absolute;top:62px;height:875px;background:var(--paper);overflow:hidden}
.sheet-shop{left:170px;width:356px}
.sheet-site{left:623px;width:455px}
.brand{position:absolute;font:700 20px/1 "Montserrat",Arial,sans-serif;color:var(--teal);white-space:nowrap}
.brand small{display:block;font:600 6px/1 "Montserrat",Arial,sans-serif;color:var(--ink);text-align:right;margin-top:3px;letter-spacing:.5px}
.trouble{position:absolute;font:600 4.5px/1 "Montserrat",Arial,sans-serif;color:#333;white-space:nowrap}
.trouble span{color:var(--sky)}
.nav{position:absolute;display:flex;justify-content:space-between;font:600 7px/1 "Montserrat",Arial,sans-serif;color:#111;white-space:nowrap}
.nav-rule{position:absolute;left:0;right:0;height:6px;background:linear-gradient(#e9e9e9,#fff)}
.photo{position:absolute}
.tile{position:absolute;overflow:hidden;border:1px solid #cfcfcf}
.promo{position:absolute;text-align:center;white-space:nowrap}
.promo-title{font:700 13px/1 "Montserrat",sans-serif;color:#fff;text-shadow:0 1px 2px rgba(0,0,0,.35)}
.promo-row{display:flex;align-items:center;justify-content:center;gap:2px;margin-top:3px}
.promo-new{background:var(--red);color:#fff;font:700 4px/1 "Montserrat",sans-serif;padding:1px 2px}
.promo-band{background:var(--teal);color:#fff;font:700 6px/1 "Montserrat",sans-serif;letter-spacing:1px;padding:3px 10px}
.promo-sub{font:700 8px/1.15 "Roboto Slab",serif;color:#fff;margin-top:4px;text-shadow:0 1px 2px rgba(0,0,0,.35)}
.foot-band{position:absolute;left:0;right:0;background:var(--band)}
.foot-note{position:absolute;left:0;right:0;text-align:center;font:600 5px/1.5 "Montserrat",sans-serif;color:#222}
.social{position:absolute;display:flex}
.social i{display:block;border-radius:4px;background:var(--sky)}
.copyright{position:absolute;left:0;right:0;text-align:center;font:600 4.5px/1 "Montserrat",sans-serif;color:#333}
.tagline{position:absolute;font:700 17px/1 "Montserrat",sans-serif;letter-spacing:.3px;white-space:nowrap}
.shop-title{font:800 16px/1 "Montserrat",sans-serif;margin-bottom:12px}
.shop-copy p{font:400 7.9px/1.3 "Montserrat",sans-serif;color:#333;margin-bottom:9px}
.service{position:absolute;top:592px;width:124px;height:130px}
.service h3{font:700 9px/1 "Montserrat",sans-serif;color:var(--teal);margin-bottom:8px;white-space:nowrap}
.service p{font:400 5.6px/9.8px "Montserrat",sans-serif;color:#333;text-align:justify}
.service a{position:absolute;right:0;top:116px;font:600 6.5px/1 "Montserrat",sans-serif;color:var(--teal);text-decoration:none}
</style>
</head>
<body>

<div class="label" style="left:172px">SHOP EMAIL TEMPLATE</div>
<div class="label" style="left:625px">WEBSITE &nbsp;EMAIL TEMPLATE</div>

<section class="sheet sheet-shop">
  <div class="brand" style="left:32px;top:22px;font-size:17px">Maren Vale<small>FINE LIVING</small></div>
  <div class="trouble" style="left:156px;top:35px">HAVING TROUBLE READING THIS EMAIL? <span>VIEW THIS EMAIL IN YOUR BROWSER.</span></div>
  <nav class="nav" style="left:27px;top:63px;width:306px;font-size:6.5px">
    <span>HOME</span><span>BATH &amp; SPA</span><span>LINEN</span><span>KITCHEN</span><span>GARDEN</span><span>TRAVEL</span><span>GIFTS</span><span>LEISURE</span>
  </nav>
  <div class="nav-rule" style="top:80px"></div>

  <div class="tile" style="left:24px;top:96px;width:308px;height:156px">
    <div class="photo" role="img" aria-label="Teak bath caddy resting across a dark soaking tub with a potted plant" style="inset:0;background:radial-gradient(ellipse 55% 22% at 40% 62%,#c79a5c,rgba(199,154,92,0) 100%),radial-gradient(ellipse 30% 40% at 35% 30%,#a9a59e,rgba(169,165,158,0) 100%),linear-gradient(180deg,#8b8781 0%,#75706a 45%,#4d433b 70%,#2f2520 100%)"></div>
    <div class="promo" style="left:184px;top:22px;width:114px">
      <div class="promo-title" style="font-size:11px">INTRODUCING ZEN</div>
      <div class="promo-row"><span class="promo-new">NEW</span><span class="promo-band" style="padding:3px 8px">TEAK COLLECTION</span></div>
      <div class="promo-sub">COMPLIMENT YOUR SPA<br>OR BATH</div>
    </div>
  </div>

  <div class="abs" style="left:24px;top:256px;width:17px;height:164px;background:#4a4440"></div>
  <div class="tile" style="left:48px;top:256px;width:160px;height:164px;background:#fff">
    <div class="photo" role="img" aria-label="Portable grill beside a cooler with lobster and grilled food" style="left:78px;top:0;width:82px;height:164px;background:radial-gradient(ellipse 45% 25% at 45% 40%,#c56a4f,rgba(197,106,79,0) 100%),radial-gradient(ellipse 60% 30% at 40% 80%,#9a9a9a,rgba(154,154,154,0) 100%),linear-gradient(160deg,#c9c9c9,#5e5e5e 55%,#2e2e2e)"></div>
    <div class="abs" style="left:8px;top:26px;font:800 13px/1 Montserrat,sans-serif">TAILGATING</div>
    <div class="abs" style="left:8px;top:41px;background:#555;color:#fff;font:700 5px/1 Montserrat,sans-serif;padding:2px 3px;white-space:nowrap">SHOP ALL TAILGATING</div>
    <div class="abs" style="left:8px;top:52px;width:112px;font:800 7px/1.1 Montserrat,sans-serif;color:var(--teal)">GET THE RIGHT GRILL TO MAKE THE MOST OF THE TAILGATING SEASON.</div>
    <div class="abs" style="left:8px;top:80px;width:62px;font:400 4px/1.5 'Open Sans',sans-serif;color:#333">Looking for portable grills, coolers and folding tables? MarenVale.com has all your tailgating supplies.</div>
  </div>
  <div class="tile" style="left:216px;top:256px;width:116px;height:79px;background:#fff">
    <div class="photo" role="img" aria-label="Polished chrome grab bars" style="left:62px;top:6px;width:48px;height:66px;background:linear-gradient(90deg,#fff 0,#cfcfcf 12%,#fff 22%,#bdbdbd 38%,#fff 50%,#c4c4c4 66%,#fff 78%,#d0d0d0 92%,#fff 100%)"></div>
    <div class="abs" style="left:7px;top:10px;font:800 10px/1 Montserrat,sans-serif">10% SALE</div>
    <div class="abs" style="left:7px;top:23px;background:var(--red);color:#fff;font:700 4px/1 Montserrat,sans-serif;padding:1px 3px">DO NOT MISS</div>
    <div class="abs" style="left:7px;top:31px;width:55px;font:600 4.5px/1.3 Montserrat,sans-serif;color:#666">ON ALL GRAB BARS ONLY THIS MONTH</div>
    <div class="abs" style="left:7px;top:55px;background:var(--red);color:#fff;font:700 4px/1 Montserrat,sans-serif;padding:2px 3px;white-space:nowrap">NO COUPON NEEDED</div>
  </div>
  <div class="tile" style="left:216px;top:340px;width:116px;height:80px">
    <div class="photo" role="img" aria-label="Enamel tableware with red lobster print" style="inset:0;background:radial-gradient(circle at 30% 65%,#d9452f 0,#e88a76 18%,rgba(240,232,226,0) 34%),radial-gradient(circle at 78% 45%,#d9452f 0,#e88a76 16%,rgba(240,232,226,0) 30%),linear-gradient(135deg,#f4f1ee,#e6ded8)"></div>
    <div class="abs" style="left:4px;top:6px;font:800 6px/1 Montserrat,sans-serif">TABLETOP</div>
  </div>

  <div class="tile" style="left:24px;top:426px;width:308px;height:69px">
    <div class="photo" role="img" aria-label="Chrome bathroom fixture against soft fabric" style="inset:0;background:radial-gradient(ellipse 25% 40% at 88% 30%,#f2f2f2,rgba(242,242,242,0) 100%),linear-gradient(180deg,#777069 0%,#a9a39b 35%,#d8d3cb 70%,#bdb7ae 100%)"></div>
    <div class="abs" style="left:61px;top:17px;width:196px;background:var(--coral);color:#fff;text-align:center;font:600 7px/1 Montserrat,sans-serif;letter-spacing:3px;padding:3px 0;white-space:nowrap">BATHROOM ACCESSORIES</div>
    <div class="abs" style="left:66px;top:32px;display:flex;font:600 5.5px/1 Montserrat,sans-serif;color:#fff;letter-spacing:1.5px;white-space:nowrap">
      <span style="background:var(--gold);padding:3px 8px">TOWEL BARS</span><span style="background:var(--teal);padding:3px 8px">BIDETS, MIRRORS</span>
    </div>
  </div>

  <div class="tile" style="left:24px;top:500px;width:152px;height:83px">
    <div class="photo" role="img" aria-label="Ceramic jugs on a wooden serving board" style="inset:0;background:radial-gradient(ellipse 35% 45% at 22% 30%,#8b9a6e,rgba(139,154,110,0) 100%),radial-gradient(ellipse 50% 25% at 55% 85%,#9b7a4e,rgba(155,122,78,0) 100%),linear-gradient(120deg,#5e6a4e,#3f3a30 55%,#6f6148)"></div>
    <div class="abs" style="left:0;right:0;top:30px;text-align:center;font:300 8px/1.1 Montserrat,sans-serif;color:#fff;letter-spacing:1.5px;white-space:nowrap">AUTHENTIC ACCENTS<br><b style="font-weight:700;letter-spacing:.5px">FOR YOUR HOME</b></div>
  </div>
  <div class="tile" style="left:180px;top:500px;width:152px;height:83px;background:#fff">
    <div class="photo" role="img" aria-label="Outdoor cushions in tropical print" style="left:0;top:0;width:66px;height:83px;background:radial-gradient(circle at 30% 70%,#2f9fbf 0,#6cc0d6 25%,rgba(238,233,206,0) 45%),radial-gradient(circle at 75% 25%,#3aa9c9 0,rgba(238,233,206,0) 35%),linear-gradient(135deg,#eee9ce,#dfe9d8)"></div>
    <div class="abs" style="left:70px;top:8px;font:800 7px/1 Montserrat,sans-serif">GARDEN STYLE</div>
    <div class="abs" style="left:70px;top:17px;background:var(--green);color:#fff;font:700 4px/1 Montserrat,sans-serif;padding:2px 3px;white-space:nowrap">FOR A POP OF COLOR!</div>
    <div class="abs" style="left:70px;top:26px;font:700 5px/1 Montserrat,sans-serif;color:var(--teal)">CHECK IT NOW!</div>
    <div class="abs" style="left:70px;top:35px;width:76px;font:400 3.8px/1.5 'Open Sans',sans-serif;color:#333">Whether you like bold prints or soft tropical tones, fresh outdoor cushions are ready for your patio.</div>
  </div>

  <div class="tile" style="left:24px;top:588px;width:152px;height:106px;background:#fff">
    <div class="abs" style="left:0;top:0;width:18px;height:106px;background:var(--teal)"></div>
    <div class="abs" style="left:3px;top:98px;transform:rotate(-90deg);transform-origin:0 0;font:700 6.5px/1 Montserrat,sans-serif;color:#fff;letter-spacing:1.5px;white-space:nowrap">TRAVELING?</div>
    <div class="abs" style="left:11px;top:98px;transform:rotate(-90deg);transform-origin:0 0;font:700 6.5px/1 Montserrat,sans-serif;color:#fff;letter-spacing:1.5px;white-space:nowrap;background:#222;padding:1px 3px">VISIT OUR SHOP</div>
    <div class="photo" role="img" aria-label="Black quilted rolling travel bag" style="left:44px;top:4px;width:96px;height:100px;background:radial-gradient(ellipse 40% 45% at 50% 55%,#4a4a4a,rgba(74,74,74,0) 100%),radial-gradient(ellipse 55% 55% at 50% 55%,#1a1a1a 0,#1a1a1a 70%,rgba(255,255,255,0) 72%)"></div>
  </div>
  <div class="tile" style="left:180px;top:588px;width:152px;height:86px">
    <div class="photo" role="img" aria-label="Stone garden statue on weathered wood" style="inset:0;background:radial-gradient(ellipse 30% 45% at 68% 50%,#d6d1c2,rgba(214,209,194,0) 100%),radial-gradient(ellipse 40% 30% at 20% 85%,#6d5e4a,rgba(109,94,74,0) 100%),linear-gradient(90deg,#7a7464,#a39d8b 55%,#8c8676)"></div>
    <div class="abs" style="left:6px;top:20px;font:400 5px/1.2 Montserrat,sans-serif;color:#fff;white-space:nowrap">CHECK OUT <b style="font-size:7px">GARDEN</b><br><b style="font-size:7px">STATUARY</b><br>AND ACCENTS</div>
  </div>
  <div class="abs" style="left:180px;top:676px;width:152px;height:18px;background:var(--lime)"></div>

  <div class="tile" style="left:24px;top:698px;width:308px;height:70px">
    <div class="photo" role="img" aria-label="Picnic on a sunny lawn with a wine basket" style="inset:0;background:radial-gradient(ellipse 30% 50% at 62% 35%,#d9c98c,rgba(217,201,140,0) 100%),radial-gradient(ellipse 30% 40% at 85% 70%,#b07a4a,rgba(176,122,74,0) 100%),linear-gradient(180deg,#8a9a4a 0%,#6b7d36 55%,#566a2a 100%)"></div>
    <div class="abs" style="left:28px;top:12px;font:300 16px/1 Montserrat,sans-serif;color:#fff;letter-spacing:5px;white-space:nowrap">LEISURE LIFE</div>
    <div class="abs" style="left:42px;top:31px;font:700 5px/1 Montserrat,sans-serif;color:#fff;white-space:nowrap">EXPERIENCE THE GREAT OUTDOORS</div>
    <div class="abs" style="left:42px;top:40px;width:160px;font:400 4.3px/1.45 'Open Sans',sans-serif;color:#fff">Picnic baskets and wine bags add romance to any outdoor dining experience. Grab a weekend bag or insulated tote and dine al fresco.</div>
  </div>

  <div class="foot-band" style="top:781px;height:52px"></div>
  <div class="brand" style="left:146px;top:789px;font-size:12px">Maren Vale<small style="font-size:4px">FINE LIVING</small></div>
  <div class="foot-note" style="top:815px;font-size:4.5px;padding:0 24px">MAREN VALE FINE LIVING IS ALL ABOUT A RELAXED, WARM AND WELCOMING LIFESTYLE. WE HAVE HANDPICKED ITEMS THAT ENHANCE THIS LIFESTYLE, AND ALLOW YOU TO LET YOUR PERSONAL STYLE SHINE THROUGH.</div>
  <div class="social" style="left:132px;top:840px;gap:9px" aria-label="Social links">
    <i style="width:16px;height:16px"></i><i style="width:16px;height:16px"></i><i style="width:16px;height:16px"></i><i style="width:16px;height:16px"></i>
  </div>
  <div class="copyright" style="top:862px;font-size:4px">© 2013 COPYRIGHT MAREN VALE ENTERPRISES &amp; MAREN VALE FINE LIVING. ALL RIGHTS RESERVED.</div>
</section>

<section class="sheet sheet-site">
  <div class="brand" style="left:38px;top:28px;font-size:22px">Maren Vale<small style="font-size:7px">FINE LIVING</small></div>
  <div class="trouble" style="left:199px;top:49px;font-size:5.5px">HAVING TROUBLE READING THIS EMAIL? <span>VIEW THIS EMAIL IN YOUR BROWSER.</span></div>
  <nav class="nav" style="left:68px;top:81px;width:326px;font-size:8.5px">
    <span>STYLE</span><span>SHOP</span><span>DESIGN</span><span>LIFE</span><span>HOME</span><span>PRESS</span><span>CONTACT</span>
  </nav>
  <div class="nav-rule" style="top:101px;height:8px"></div>

  <div class="tagline" style="left:35px;top:129px">WHERE REAL LIFE MEETS REAL STYLE</div>

  <div class="photo" role="img" aria-label="Dark stone bath vanity with a sculptural vase and a wall faucet" style="left:0;top:158px;width:455px;height:183px;background:radial-gradient(ellipse 8% 14% at 30% 22%,#a7a7a5,rgba(167,167,165,0) 100%),radial-gradient(ellipse 14% 40% at 90% 60%,#5a4636,rgba(90,70,54,0) 100%),linear-gradient(180deg,rgba(0,0,0,0) 0,rgba(0,0,0,0) 40%,rgba(10,10,10,.55) 42%,rgba(10,10,10,.8) 100%),linear-gradient(100deg,#9a9996,#6f6e6b 18%,#3a3a39 30%,#2c2c2c 62%,#6a6966 78%,#8f8e8b)"></div>
  <div class="promo" style="left:118px;top:267px;width:170px">
    <div class="promo-title">INTRODUCING ZEN</div>
    <div class="promo-row"><span class="promo-new">NEW</span><span class="promo-band" style="font-size:7px;padding:3px 18px">TEAK COLLECTION</span></div>
    <div class="promo-sub" style="font-family:Montserrat,sans-serif;font-size:8px">COMPLIMENT YOUR SPA<br>OR BATH</div>
  </div>

  <div class="abs" style="left:0;top:341px;width:455px;height:232px;background:var(--band)"></div>
  <div class="abs shop-copy" style="left:31px;top:370px;width:230px">
    <h2 class="shop-title">SHOP MAREN VALE</h2>
    <p>Maren Vale Fine Living is all about a relaxed, warm and welcoming lifestyle. We have handpicked items that enhance this lifestyle, and allow you to let your personal style shine through.</p>
    <p>Explore our style and safety that our spa bathroom products can bring to your home. Our kitchen and entertaining items will surely set you apart as a welcoming hostess. You will also find an incredible selection of unique and tasteful gifts for everyone on your list.</p>
    <p>You will find designer notes throughout the site to give you extra product information and make your shopping choices easier.</p>
  </div>
  <div class="photo" role="img" aria-label="Preview of the online shop page" style="left:284px;top:393px;width:142px;height:142px;border-radius:50%;background:radial-gradient(ellipse 35% 22% at 30% 55%,#8a6a44,rgba(138,106,68,0) 100%),linear-gradient(180deg,#fafafa 0,#fafafa 22%,#5a5752 24%,#4a4743 60%,#e6e6e6 62%,#cfd6da 100%)"></div>

  <article class="service" style="left:31px">
    <h3>DESIGN SERVICES</h3>
    <p>From Blueprints to Bubbles....The design process is fun and exciting without being overwhelming. We help clients create a home that reflects their own personal style. Whether we are purchasing new decor pieces, highlighting discoveries from past travel adventures, or weaving in cherished personal possessions it is our goal to make sure our clients find their perfect balance between style and function.</p>
    <a href="#">READ MORE &gt;</a>
  </article>
  <article class="service" style="left:165px">
    <h3>CONCIERGE &nbsp;SERVICES</h3>
    <p>Whether our clients are here for the season or just a long weekend, we provide the ease and comfort of having concierge services available to help with everything from dinner reservations, fishing excursions, babysitting and refrigerator stocking. It is our goal to make you and your guests in time Harbor Bay extra special. Open the front door and enjoy!</p>
    <a href="#">READ MORE &gt;</a>
  </article>
  <article class="service" style="left:301px">
    <h3>HOME MANAGE MENT</h3>
    <p>Properly maintaining homes of exceptional quality and value is a year round job. We take the stress out of this process making our clients' arrivals and departures throughout the year are relaxed and enjoyable. Our team makes sure that all mechanical maintenance, deep cleaning, and regular repairs are performed on a regular basis. Let us take care of Linecast while you are on the golf course or enjoying the beach.</p>
    <a href="#">READ MORE &gt;</a>
  </article>

  <div class="foot-band" style="top:746px;height:64px"></div>
  <div class="brand" style="left:186px;top:755px;font-size:15px">Maren Vale<small style="font-size:5px">FINE LIVING</small></div>
  <div class="foot-note" style="top:784px;padding:0 30px">MAREN VALE FINE LIVING IS ALL ABOUT A RELAXED, WARM AND WELCOMING LIFESTYLE. WE HAVE HANDPICKED ITEMS THAT ENHANCE THIS LIFESTYLE, AND ALLOW YOU TO LET YOUR PERSONAL STYLE SHINE THROUGH.</div>
  <div class="social" style="left:169px;top:817px;gap:11px" aria-label="Social links">
    <i style="width:23px;height:23px"></i><i style="width:23px;height:23px"></i><i style="width:23px;height:23px"></i><i style="width:23px;height:23px"></i>
  </div>
  <div class="copyright" style="top:848px;font-size:5.5px">© 2013 COPYRIGHT MAREN VALE ENTERPRISES &amp; MAREN VALE FINE LIVING. ALL RIGHTS RESERVED.</div>
</section>

</body>
</html>
```